Powerpoint Design for business and consulting company - Dorneck-Saalig

I am searching a design specialist who can help me to create a PowerPoint Design for my company. I'm in the business coaching and consulting industry.

The PPT master should be easy to use and include professional formatting (using the fonts of my website). In general, the slide master should have the look and feel of my website (in terms of fonts, colors, logos, possibility to place big photographs, having text and graph slides as well as photo slides with just 1 key message).

The PowerPoint design should fit my cooperate Identity (please see my website https://dorneck-saalig.de).
My logos are attached.

Additional information:
- wide screen format - 16: 9
- right set up of a fitting color scheme
https: // farbwexo. io / f6ded1-bfcbce-807f84-9cd3d1-666666
# 666666 (Dim Gray) - body / heading text
# 807F84 (Gray Web)
#BFCBCE (Silver Sand) - link hover
# 9cd3d1 (Powder Blue) - Link color
# F6DED1 (Champagne Pink)

- creation of chart templates, using chart tools, and different chart types etc.
- creation of different slide layouts to place content, pictures (in different sizes), optionally Media
- set up of display guide lines
- as well as standard elements, such as text boxes, lines, default shapes, etc.

Requirements
Must have
• Powerpoint Design needs to have:
https://farbwexo.io/f6ded1-bfcbce-807f84-9cd3d1-666666
# 807F84 (Gray Web)
# F6DED1 (Champagne Pink)

```html
<!DOCTYPE html>
<html lang="en">
<head>
<meta charset="utf-8">
<title>Presentation Title – Helene Dorneck-Saalig</title>
<link rel="stylesheet" href="https://fonts.googleapis.com/css2?family=Open+Sans:wdth,wght@75..100,300..800&display=swap">
<style>
  :root {
    --canvas: #ffffff;
    --title: #2f2a2a;
    --body: #666666;
    --gray-web: #807f84;
    --champagne: #f6ded1;
    --brand: #1f1c1c;
    --photo-dark: #8a8a8a;
    --photo-mid: #c6c6c6;
    --photo-light: #e4e4e4;
    --photo-ground: #b4b4b4;
  }
  html, body {
    margin: 0;
    padding: 0;
    overflow: hidden;
    background: var(--canvas);
  }
  .slide {
    position: relative;
    width: 1200px;
    height: 674px;
    overflow: hidden;
    background: var(--canvas);
    font-family: "Open Sans", Arial, sans-serif;
  }
  .hero-photo {
    position: absolute;
    left: 0;
    top: 0;
    width: 680px;
    height: 674px;
    background:
      linear-gradient(to right, rgba(255,255,255,0) 0%, rgba(255,255,255,0) 58%, rgba(246,222,209,0.35) 80%, #ffffff 100%),
      linear-gradient(to bottom, var(--photo-dark) 0%, var(--photo-mid) 36%, var(--photo-light) 58%, #d2d2d2 78%, var(--photo-ground) 100%);
  }
  .brand {
    position: absolute;
    left: 580px;
    top: 110px;
    display: flex;
    align-items: center;
    gap: 12px;
    color: var(--brand);
  }
  .brand-mark {
    width: 40px;
    height: 40px;
    border-radius: 50%;
    background: var(--champagne);
  }
  .brand-name {
    font-size: 16px;
    font-weight: 400;
    line-height: 1.1;
    text-transform: lowercase;
  }
  .title {
    position: absolute;
    left: 577px;
    top: 262px;
    margin: 0;
    font-size: 51px;
    font-weight: 700;
    font-stretch: 88%;
    letter-spacing: 1.6px;
    color: var(--title);
    white-space: nowrap;
  }
  .subtitle {
    position: absolute;
    left: 580px;
    top: 326px;
    width: 540px;
    margin: 0;
    font-size: 19px;
    font-weight: 300;
    line-height: 1.3;
    color: var(--body);
  }
  .footnote {
    position: absolute;
    left: 578px;
    top: 565px;
    width: 525px;
    margin: 0;
    font-size: 14.5px;
    font-weight: 300;
    line-height: 1.3;
    color: var(--gray-web);
  }
</style>
</head>
<body>
  <main class="slide">
    <div class="hero-photo" role="img" aria-label="Black-and-white photograph of a river promenade with an arched bridge and city buildings under a cloudy sky, fading into white"></div>

    <div class="brand">
      <span class="brand-mark"></span>
      <span class="brand-name">helene<br>dorneck-saalig</span>
    </div>

    <h1 class="title">PRESENTATION TITLE</h1>
    <p class="subtitle">Aspernatur magni aperiam veritat beatae volu doloremque perspiciatis error consequuntur ipsa aspernatur</p>

    <p class="footnote">Aspernatur magni quae aperiam aut veritati beatae voluptas doloremque perspiciatis error consequuntur ipsa aspernatur iste</p>
  </main>
</body>
</html>
```